Wedding Program

Miriam and Owen are getting married. They are looking for a simple 4-page program that conveys the special day. Venue is a museum in a large East-Coast city: classic 18th century, formal. Ceremony is non-religious. Party includes a photo booth and DJ.

He's a math geek - she's an activist/educator.

Please incorporate unique design sensibility - be creative! Colors of purple, eggplant, ivory, and gray are the couple's choice. Fall motif OK.

Target Market(s)

ages 25 - 85, members of a family

Industry/Entity Type

Graphic Design

Font styles to use
Serif
Decorative

Colors
8769ae
b7a5cd
fece3e
f78f20
757575
cfcfcf
6b449b
a64599
fffaee

Requirements
Must have
• Readable, attractive 4-color design using the copy and image provided in the attachment.
Nice to have
• It's a LOVE-ly day for a wedding - be creative!
Should not have
• Avoid flowery girly-girl fonts or obvious hearts and flowers stuff.

```html
<!DOCTYPE html>
<html lang="en">
<head>
<meta charset="utf-8">
<title>To our Wedding Guests</title>
<link href="https://fonts.googleapis.com/css2?family=Cormorant+SC:wght@500;600&family=Cormorant+Garamond:ital,wght@1,500&family=Parisienne&display=swap" rel="stylesheet">
<style>
  :root {
    --ivory: #fffaee;
    --lace: #fbdcb8;
    --lace-soft: #fdebd4;
    --tangerine: #f59a3a;
    --ink: #2b2622;
    --ink-soft: #3e3832;
    --photo-dark: #3a3424;
    --photo-mid: #6f6a4e;
    --photo-light: #a79f84;
  }
  * { margin: 0; padding: 0; box-sizing: border-box; }
  html, body { width: 857px; height: 1200px; overflow: hidden; background: var(--ivory); }
  .program-page {
    position: relative;
    width: 857px;
    height: 1200px;
    background: var(--ivory);
    overflow: hidden;
  }
  .lace-backdrop {
    position: absolute;
    left: 0; top: 0;
    width: 857px; height: 810px;
    background:
      radial-gradient(ellipse 60% 30% at 50% 18%, var(--lace) 0%, transparent 70%),
      radial-gradient(ellipse 45% 25% at 15% 8%, var(--lace-soft) 0%, transparent 70%),
      radial-gradient(ellipse 45% 25% at 85% 8%, var(--lace-soft) 0%, transparent 70%),
      linear-gradient(180deg, var(--lace-soft) 0%, var(--ivory) 75%);
  }
  .welcome {
    position: absolute;
    left: 0; top: 0;
    width: 857px;
    text-align: center;
    color: var(--ink);
  }
  .welcome-title {
    position: absolute;
    top: 262px;
    width: 100%;
    font-family: "Parisienne", cursive;
    font-weight: 400;
    font-size: 58px;
    color: var(--tangerine);
    letter-spacing: 1px;
  }
  .welcome-text {
    position: absolute;
    width: 100%;
    font-family: "Cormorant SC", serif;
    font-weight: 600;
    color: var(--ink);
  }
  .welcome-text.opening { top: 354px; font-size: 23px; line-height: 29px; }
  .welcome-text.vows {
    top: 494px;
    font-family: "Cormorant Garamond", serif;
    font-style: italic;
    font-weight: 500;
    font-variant: small-caps;
    font-size: 22px;
    line-height: 32px;
    color: var(--ink-soft);
  }
  .welcome-text.closing { top: 606px; font-size: 25px; line-height: 35px; }
  .couple-photo {
    position: absolute;
    left: 0; top: 810px;
    width: 857px; height: 390px;
    background:
      radial-gradient(ellipse 30% 45% at 45% 70%, #5a3a3a 0%, transparent 70%),
      radial-gradient(ellipse 25% 45% at 80% 60%, #7a6050 0%, transparent 70%),
      linear-gradient(90deg, var(--photo-mid) 0%, var(--photo-light) 30%, var(--photo-mid) 55%, var(--photo-dark) 100%);
  }
</style>
</head>
<body>
  <main class="program-page">
    <div class="lace-backdrop" role="img" aria-label="Soft peach lace pattern background"></div>
    <section class="welcome">
      <h1 class="welcome-title">To our Wedding Guests</h1>
      <p class="welcome-text opening">Your presence here adds greatly to our joy and happiness on this special day.<br>Today marks the beginning of our lives together.</p>
      <p class="welcome-text vows">We stand before you now, declaring<br>our love for each other and for our intent to be joined in marriage.<br>We share with each other without reservation our lives, fortunes and future.</p>
      <p class="welcome-text closing">We hope that you will continue to wish us well<br>in our new life and we are grateful to have your love,<br>care and best wishes for today and always!</p>
    </section>
    <div class="couple-photo" role="img" aria-label="Photograph of the couple smiling together in front of bamboo"></div>
  </main>
</body>
</html>
```